Weather of the Heart Is the Ledger A Novel by Carl Whitby and Martin Holloway

Weather of the Heart Is the Ledger is a business novel about leadership, follower-ship, resilience, and insight.
It follows a high-performing executive whose conventional management tools and techniques stop working during a professional crisis. His transformation does not come from new strategies or tactics, but from a fundamentally different understanding of how mindset shapes performance, decision-making, leadership and follower-ship. Through the course of the book, the executive, his team, and his customers realize that “State of Mind” (healthy psychological functioning) is the horsepower that drives business and life.
This is not a self-help book, textbook, or memoir. It is thoughtful business fiction with philosophical depth.

Introduction/Preface for the novel:
We wrote this book because something profound changed the way we live, work, and lead. Over the course of several decades - across boardrooms, high-stakes corporate challenges, private practice, and moments of quiet personal insight - we began to see a deeper truth about the human experience. It was a truth that, once seen, dramatically improved the quality of our lives, and the lives of the people with whom we worked.
That truth comes from understanding the Three Principles of Mind, Consciousness, and Thought, as discovered and first articulated by the philosopher and theosopher, Edwin Thorley. Though simple, these Principles point to something universally powerful—how all people experience life from the inside out. When understood, they reveal a level of clarity, resilience, and well-being that can transform not only individuals, but entire organizations.
At first, we tried to write a traditional business book—a primer designed to share how understanding the Principles can lead to more grounded, wise, and effective leadership—without the need for techniques or tools. But as we wrote, we found ourselves returning again and again to stories. Real stories. Composite stories. Fictional ones. We realized that the best way to share this understanding wasn’t through frameworks or prescriptive advice. It was through story.
So, we created one big story.
This novel is the result. Though fictional, it is inspired by real patterns, real shifts, and real struggles we’ve lived through and witnessed over decades of work, together and separately. The characters are inventions, but their experiences are familiar. We’ve watched people just like them transform—from confusion to clarity, from fear to resilience, from burnout to wisdom.
Our hope is that this book moves you—not just as a story, but as an experience. We believe that the ideas woven into Owen Castell’s journey can help anyone live with greater ease, purpose, and peace of mind. Whether you lead a Fortune 500 company or a family of five, what’s offered here is for you.
And if something in this story helps you see your own life with fresh eyes, then the book has done its job.
Welcome to the journey.
—Carl & Martin

Target Market(s)

• Senior leaders, executives, and high-potential managers • Business professionals experiencing pressure, burnout, or diminishing returns from traditional leadership approaches • Leadership coaches and organizational consultants • Readers of intelligent, reflective business fiction or non-business people who are interested in what makes people tick — and achieve their highest potential Tone should appeal to serious, experienced professionals, not beginners or hype-seekers.

Industry/Entity Type

• Business / Leadership / Psychology • Business Fiction • Leadership Novel

Font styles to use
Serif

Colors
0054AA
0677BA
7BADD7
CADEEF
E8F1F8

Requirements
Must have
• We are looking for metaphorical representations of: • A fork in the road • A deviation from the conventional path (that makes all the difference) • One element choosing a different direction—not running away, not rebelling, just seeing differently Think quiet insight, not drama. Must-Haves • Clear, legible title at thumbnail size • A visual metaphor for choice or alternate thinking • Professional, credible aesthetic • Obvious that this is fiction (a novel), not a textbook • Clean typography (no clutter)
Nice to have
• • A sense of motion or transition • Minimalist or restrained color palette • One accent element that signifies insight or departure from convention • Timeless design (should still feel current in 5 or 10 years)
Should not have
• • Literal business clichés (gears, ladders, chess pieces, lightbulbs, compasses, eagles) • Stock-photo people in suits • “Hero CEO” imagery • Overly mystical or “woo-woo” visuals • Aggressive, macho, or hustle-culture tone • Anything cartoonish or silly

```html
<!DOCTYPE html>
<html lang="en">
<head>
<meta charset="utf-8">
<title>Weather of the Heart Is the Ledger — Cover</title>
<link rel="stylesheet" href="https://fonts.googleapis.com/css2?family=Playfair+Display:wght@700&family=Libre+Baskerville:wght@400&display=swap">
<style>
  :root {
    --page-bg: #f2f2f2;
    --deep-blue: #0054AA;
    --mid-blue: #0677BA;
    --soft-blue: #7BADD7;
    --pale-blue: #CADEEF;
    --mist-blue: #E8F1F8;
    --white: #ffffff;
  }
  * { margin: 0; padding: 0; box-sizing: border-box; }
  html, body {
    width: 1196px;
    height: 1200px;
    overflow: hidden;
    background: var(--page-bg);
  }
  .cover {
    position: absolute;
    left: 208px;
    top: 15px;
    width: 780px;
    height: 1170px;
    overflow: hidden;
    background: linear-gradient(180deg, var(--mist-blue) 0%, var(--white) 45%, var(--white) 100%);
  }
  .cover__title {
    position: absolute;
    left: 0;
    right: 0;
    top: 70px;
    text-align: center;
    font-family: "Playfair Display", Georgia, serif;
    font-weight: 700;
    font-size: 80px;
    line-height: 98px;
    letter-spacing: 1px;
    text-transform: uppercase;
    color: var(--deep-blue);
  }
  .cover__title span { display: block; }
  .cover__title .cover__title-accent { color: var(--mid-blue); }
  .cover__scene {
    position: absolute;
    left: 0;
    right: 0;
    top: 440px;
    height: 620px;
    background:
      radial-gradient(ellipse 60% 55% at 50% 60%, var(--pale-blue) 0%, transparent 100%),
      linear-gradient(180deg, transparent 0%, var(--mist-blue) 45%, transparent 100%);
  }
  .cover__fork {
    position: absolute;
    inset: 0;
    width: 100%;
    height: 100%;
  }
  .cover__authors {
    position: absolute;
    left: 0;
    right: 0;
    top: 1088px;
    text-align: center;
    font-family: "Libre Baskerville", Georgia, serif;
    font-size: 24px;
    line-height: 30px;
    letter-spacing: 3px;
    text-transform: uppercase;
    color: var(--deep-blue);
  }
</style>
</head>
<body>
  <main class="cover">
    <h1 class="cover__title">
      <span>Weather of</span>
      <span>the Heart Is</span>
      <span class="cover__title-accent">the Ledger</span>
    </h1>
    <div class="cover__scene" role="img" aria-label="Soft blue landscape where a single path divides, one branch quietly turning aside">
      <svg class="cover__fork" viewBox="0 0 780 620" aria-hidden="true">
        <defs>
          <linearGradient id="road-main" x1="0" y1="1" x2="0" y2="0">
            <stop offset="0" stop-color="#7BADD7" stop-opacity="0.9"/>
            <stop offset="1" stop-color="#CADEEF" stop-opacity="0"/>
          </linearGradient>
          <linearGradient id="road-branch" x1="0" y1="1" x2="1" y2="0">
            <stop offset="0" stop-color="#0677BA"/>
            <stop offset="1" stop-color="#0054AA"/>
          </linearGradient>
        </defs>
        <path d="M390 620 L390 60" fill="none" stroke="url(#road-main)" stroke-width="6" stroke-linecap="round"/>
        <path d="M350 620 L372 60" fill="none" stroke="url(#road-main)" stroke-width="2"/>
        <path d="M430 620 L408 60" fill="none" stroke="url(#road-main)" stroke-width="2"/>
        <path d="M390 400 C 400 300, 480 230, 590 170" fill="none" stroke="url(#road-branch)" stroke-width="6" stroke-linecap="round"/>
        <circle cx="600" cy="164" r="9" fill="#0054AA"/>
      </svg>
    </div>
    <p class="cover__authors">Carl Whitby and Martin Holloway</p>
  </main>
</body>
</html>
```